Business Card

Yes I would like you to design me a business card with the logo you just made me

Industry/Entity Type

Business

Colors
33b7a4
00a990
333333
000000
757575
7f7f7f

```html
<!DOCTYPE html>
<html lang="en">
<head>
<meta charset="utf-8">
<title>Marela Costin Photography – Business Card</title>
<link rel="stylesheet" href="https://fonts.googleapis.com/css2?family=Open+Sans:wght@400;700&display=swap">
<style>
  :root {
    --teal: #33b7a4;
    --teal-deep: #00a990;
    --paper: #ffffff;
    --backdrop: #4a4a4a;
    --ink-dark: #333333;
  }
  * { margin: 0; padding: 0; box-sizing: border-box; }
  html, body {
    width: 1200px;
    height: 691px;
    overflow: hidden;
    background: var(--backdrop);
    font-family: "Open Sans", sans-serif;
  }
  .canvas {
    position: relative;
    width: 1200px;
    height: 691px;
  }
  .card {
    position: absolute;
    top: 200px;
    width: 510px;
    height: 292px;
    box-shadow: 0 10px 24px rgba(0,0,0,0.35);
  }
  .card--front {
    left: 50px;
    background: var(--teal);
    display: flex;
    flex-direction: column;
    align-items: center;
    justify-content: center;
    gap: 12px;
  }
  .front-mark {
    width: 112px;
    height: 112px;
    border-radius: 50%;
    background: var(--paper);
  }
  .front-name {
    color: var(--paper);
    font-size: 15px;
    font-weight: 400;
    letter-spacing: 1px;
  }
  .card--back {
    left: 640px;
    background: var(--paper);
    color: var(--teal);
    text-align: center;
    padding-top: 18px;
  }
  .brand {
    display: flex;
    align-items: center;
    justify-content: center;
    gap: 8px;
  }
  .brand-dot {
    width: 48px;
    height: 48px;
    border-radius: 50%;
    background: var(--teal);
  }
  .brand-name {
    font-size: 24px;
    font-weight: 400;
    color: var(--teal);
  }
  .title {
    margin-top: 20px;
    font-size: 16px;
    font-weight: 700;
    letter-spacing: 0.5px;
  }
  .contacts {
    margin-top: 18px;
    list-style: none;
    font-size: 14.5px;
    line-height: 21px;
  }
  .contacts li {
    display: flex;
    align-items: center;
    justify-content: center;
    gap: 5px;
  }
  .contacts svg { display: block; }
  .social-square {
    width: 16px;
    height: 16px;
    border-radius: 2px;
    background: var(--teal);
  }
  .location {
    margin-top: 16px;
    font-size: 17px;
  }
</style>
</head>
<body>
<main class="canvas">
  <section class="card card--front" aria-label="Card front">
    <div class="front-mark"></div>
    <p class="front-name">marela costin</p>
  </section>

  <section class="card card--back" aria-label="Card back">
    <div class="brand">
      <div class="brand-dot"></div>
      <span class="brand-name">marela costin photography</span>
    </div>
    <h1 class="title">MARELA COSTIN | PHOTOGRAPHER</h1>
    <ul class="contacts">
      <li>
        <svg width="14" height="14" viewBox="0 0 24 24" aria-hidden="true"><path fill="#33b7a4" d="M6.6 10.8a15.2 15.2 0 0 0 6.6 6.6l2.2-2.2a1 1 0 0 1 1-.25 11.4 11.4 0 0 0 3.6.57 1 1 0 0 1 1 1V20a1 1 0 0 1-1 1A17 17 0 0 1 3 4a1 1 0 0 1 1-1h3.5a1 1 0 0 1 1 1c0 1.25.2 2.45.57 3.57a1 1 0 0 1-.25 1z"/></svg>
        <span>555.014.2290</span>
      </li>
      <li>
        <svg width="15" height="12" viewBox="0 0 24 18" aria-hidden="true"><rect x="1" y="1" width="22" height="16" fill="none" stroke="#33b7a4" stroke-width="2"/><path d="M1 1l11 9 11-9" fill="none" stroke="#33b7a4" stroke-width="2"/></svg>
        <span>marelacostinphoto@mailbox.com</span>
      </li>
      <li>
        <span class="social-square"></span>
        <span>social.example/marelacostinphotography</span>
      </li>
    </ul>
    <p class="location">Linfield MA 02190</p>
  </section>
</main>
</body>
</html>
```